Kestrel Ridge Plumbing Business card & letter head design

We need a new business card and letter head for our plumbing company called kestrel ridge plumbing. attached is the companys logo. We provide domestic and commercial plumbing services in regional western Australia. We are after Something simple yet nice to look at and something that fits within the trade industry.

Target Market(s)

trade/building industry

Contact Information for Business Card

Tarek Holm
Manager
0481 362 714
enquiries@krplumbing.example.au
ABN: 47 153 806 924
PCL: 5318

Domestic & Commercial Plumbing
Tip Truck & Excavator hire

Colors

Designer to choose colors to be used in the design.

```html
<!DOCTYPE html>
<html lang="en">
<head>
<meta charset="utf-8">
<title>Kestrel Ridge Plumbing – Letterhead &amp; Business Cards</title>
<link rel="stylesheet" href="https://fonts.googleapis.com/css2?family=Montserrat:wght@500;600;700&family=Open+Sans:wght@400&display=swap">
<style>
  :root {
    --brand-blue: #2576bc;
    --brand-grey: #4d4f53;
    --text-dark: #3a3a3a;
    --text-muted: #555;
    --paper: #ffffff;
    --paper-edge: #e2e4e8;
    --backdrop: #ffffff;
  }
  * { box-sizing: border-box; margin: 0; padding: 0; }
  html, body { width: 1200px; height: 1000px; overflow: hidden; background: var(--backdrop); }
  body { position: relative; font-family: "Open Sans", Arial, sans-serif; color: var(--text-dark); }

  .sheet { position: absolute; background: var(--paper); border: 1px solid var(--paper-edge); overflow: hidden; }

  /* Wordmark */
  .wordmark { position: absolute; font-family: "Montserrat", Arial, sans-serif; font-weight: 700; color: var(--brand-blue); text-align: center; line-height: 1.1; }
  .wordmark span { display: block; }
  .wordmark .trade { letter-spacing: 0.35em; }

  /* Icons */
  .icon { width: 14px; height: 14px; display: block; flex: none; }
  .contact-row { display: flex; align-items: center; white-space: nowrap; }

  /* Letterhead */
  .letterhead { left: 67px; top: 83px; width: 595px; height: 842px; }
  .letterhead .side-tab { position: absolute; left: 0; top: 38px; width: 22px; height: 104px; background: var(--brand-blue); }
  .letterhead .wordmark { left: 62px; top: 62px; width: 180px; font-size: 17px; }
  .letterhead .wordmark .trade { font-size: 11px; }
  .letterhead .contacts { position: absolute; right: 44px; top: 64px; text-align: right; font-family: "Open Sans", Arial, sans-serif; font-size: 8px; color: var(--text-dark); }
  .letterhead .contacts .contact-row { justify-content: flex-end; gap: 8px; height: 18px; }
  .letterhead .contacts .icon-rule { position: absolute; right: -4px; top: 2px; width: 2px; height: 49px; background: var(--brand-grey); }
  .letterhead .contacts .reg { margin-right: 22px; line-height: 11px; }
  .letterhead .head-rule { position: absolute; left: 57px; top: 143px; width: 538px; height: 3px; background: linear-gradient(90deg, var(--brand-blue) 0%, #6a9fd3 60%, rgba(255,255,255,0) 100%); }

  .letter { position: absolute; left: 33px; top: 228px; width: 550px; font-size: 10.6px; line-height: 14.6px; color: var(--text-muted); }
  .letter .date { position: absolute; left: 396px; top: 0; }
  .letter .recipient { padding-top: 13px; }
  .letter p { margin-top: 14.6px; }
  .letter .body-para { margin-top: 0; }
  .letter .signature-slot { padding-left: 3px; }
  .letter .signer { margin-top: 29px; }

  .letterhead .foot-rule { position: absolute; left: 0; top: 777px; width: 100%; height: 4px; background: var(--brand-grey); }
  .letterhead .foot-band { position: absolute; left: 0; top: 792px; width: 100%; height: 50px; background: var(--brand-blue); }

  /* Business cards */
  .card { left: 727px; width: 404px; height: 242px; }
  .card .foot-rule { position: absolute; left: 0; top: 203px; width: 100%; height: 3px; background: var(--brand-grey); }
  .card .foot-band { position: absolute; left: 0; top: 213px; width: 100%; height: 29px; background: var(--brand-blue); }

  .card-front { top: 181px; }
  .card-front .wordmark { left: 22px; top: 82px; width: 150px; font-size: 15px; }
  .card-front .wordmark .trade { font-size: 10px; }
  .card-front .holder { position: absolute; left: 189px; top: 69px; font-family: "Montserrat", Arial, sans-serif; }
  .card-front .holder-name { font-size: 13px; font-weight: 700; color: var(--brand-blue); }
  .card-front .holder-role { font-size: 10px; font-weight: 600; color: var(--brand-grey); letter-spacing: 0.04em; }
  .card-front .details { position: absolute; left: 189px; top: 101px; width: 208px; font-family: "Open Sans", Arial, sans-serif; font-size: 10.5px; color: var(--text-dark); }
  .card-front .details .icon-rule { position: absolute; left: 2px; top: 0; width: 2px; height: 58px; background: var(--brand-grey); }
  .card-front .details .contact-row { height: 20px; gap: 8px; padding-left: 7px; }
  .card-front .details .reg { padding-left: 31px; line-height: 14px; margin-top: 1px; }

  .card-back { top: 487px; }
  .card-back .wordmark { left: 127px; top: 76px; width: 150px; font-size: 15px; }
  .card-back .wordmark .trade { font-size: 10px; }
</style>
</head>
<body>

<section class="sheet letterhead" aria-label="Letterhead">
  <div class="side-tab"></div>
  <div class="wordmark"><span>KESTREL RIDGE</span><span class="trade">PLUMBING</span></div>

  <div class="contacts">
    <div class="icon-rule"></div>
    <div class="contact-row">0481 362 714
      <svg class="icon" viewBox="0 0 14 14"><rect width="14" height="14" fill="var(--brand-blue)"/><rect x="4.5" y="2.5" width="5" height="9" rx="1" fill="none" stroke="#fff"/></svg>
    </div>
    <div class="contact-row">enquiries@krplumbing.example.au
      <svg class="icon" viewBox="0 0 14 14"><rect width="14" height="14" fill="var(--brand-blue)"/><rect x="3" y="4" width="8" height="6" fill="none" stroke="#fff"/><path d="M3 4l4 3.5L11 4" fill="none" stroke="#fff"/></svg>
    </div>
    <div class="contact-row">www.krplumbing.example.au
      <svg class="icon" viewBox="0 0 14 14"><rect width="14" height="14" fill="var(--brand-blue)"/><rect x="3" y="3" width="8" height="6" fill="none" stroke="#fff"/><path d="M5 11.5h4M7 9v2.5" stroke="#fff"/></svg>
    </div>
    <div class="reg">ABN: 47 153 806 924<br>PCL: 5318</div>
  </div>
  <div class="head-rule"></div>

  <div class="letter">
    <div class="date">December 03, 2019</div>
    <div class="recipient">Mr. Dale Porter<br>Porter Building Co.<br>18 Harbour Road<br>Geraldton, WA 6530</div>
    <p>Dear Mr. Porter:</p>
    <p>The first paragraph of a typical business letter is used to state the main point of the letter. Begin with a friendly opening; then quickly transition into the purpose of your letter. Use a couple of sentences to explain the purpose, but do not go in to detail until the next paragraph.</p>
    <p class="body-para">Beginning with the second paragraph, state the supporting details to justify your purpose. These may take the form of background information, statistics or first-hand accounts. A few short paragraphs within the body of the letter should be enough to support your reasoning.</p>
    <p class="body-para">Finally, in the closing paragraph, briefly restate your purpose and why it is important. If the purpose of your letter is related to your employment, consider ending your letter with your contact information and title if it not included on letterhead. However, if the purpose is informational, think about closing with gratitude for the reader’s time.</p>
    <p>Sincerely,</p>
    <p class="signature-slot">&lt;SIGNATURE GOES HERE&gt;</p>
    <p class="signer">Mira Lowe<br>President</p>
  </div>

  <div class="foot-rule"></div>
  <div class="foot-band"></div>
</section>

<section class="sheet card card-front" aria-label="Business card front">
  <div class="wordmark"><span>KESTREL RIDGE</span><span class="trade">PLUMBING</span></div>
  <div class="holder">
    <div class="holder-name">Tarek Holm</div>
    <div class="holder-role">MANAGER</div>
  </div>
  <div class="details">
    <div class="icon-rule"></div>
    <div class="contact-row">
      <svg class="icon" viewBox="0 0 14 14"><rect width="14" height="14" fill="var(--brand-blue)"/><rect x="4.5" y="2.5" width="5" height="9" rx="1" fill="none" stroke="#fff"/></svg>
      0481 362 714
    </div>
    <div class="contact-row">
      <svg class="icon" viewBox="0 0 14 14"><rect width="14" height="14" fill="var(--brand-blue)"/><rect x="3" y="4" width="8" height="6" fill="none" stroke="#fff"/><path d="M3 4l4 3.5L11 4" fill="none" stroke="#fff"/></svg>
      enquiries@krplumbing.example.au
    </div>
    <div class="contact-row">
      <svg class="icon" viewBox="0 0 14 14"><rect width="14" height="14" fill="var(--brand-blue)"/><rect x="3" y="3" width="8" height="6" fill="none" stroke="#fff"/><path d="M5 11.5h4M7 9v2.5" stroke="#fff"/></svg>
      www.krplumbing.example.au
    </div>
    <div class="reg">ABN: 47 153 806 924<br>PCL: 5318</div>
  </div>
  <div class="foot-rule"></div>
  <div class="foot-band"></div>
</section>

<section class="sheet card card-back" aria-label="Business card back">
  <div class="wordmark"><span>KESTREL RIDGE</span><span class="trade">PLUMBING</span></div>
  <div class="foot-rule"></div>
  <div class="foot-band"></div>
</section>

</body>
</html>
```